Display Ad for Local Publication

We have never advertised before but now I would like to have an ad running in our local, community magazine. Our business is Cedar Hollow Mini Storage located in Port Ludlow, WA. PL is a small community (+/-2,500 people located across the Puget Sound from Seattle. The monthly magazine, The Tidings, covers all kinds of local news and activities and carries a number of ads from local businesses. Our is the only mini storage in Port Ludlow. We have enclosed storage units of various sizes and outdoor parking spaces for boats, trailers and RVs. I am enclosing a business card and the size requirements for Tidings advertisements. I want to develop a 1/8 page ad.

```html
<!DOCTYPE html>
<html lang="en">
<head>
<meta charset="utf-8">
<title>Cedar Hollow Mini Storage – Display Ad</title>
<link href="https://fonts.googleapis.com/css2?family=Anton&family=Barlow+Condensed:ital,wght@0,500;1,700;1,800&family=Barlow+Semi+Condensed:ital,wght@1,800&display=swap" rel="stylesheet">
<style>
  :root {
    --brand-green: #55bd5d;
    --ink: #000000;
    --paper: #ffffff;
    --photo-light: #c9d8c4;
    --photo-mid: #7cc66f;
    --photo-warm: #a88c62;
  }
  * { margin: 0; padding: 0; box-sizing: border-box; }
  html, body { width: 1200px; height: 791px; overflow: hidden; background: var(--paper); }
  .ad {
    position: relative;
    width: 1200px;
    height: 791px;
    overflow: hidden;
    background: var(--paper);
  }
  .ad-shapes, .ad-photo {
    position: absolute;
    inset: 0;
    width: 1200px;
    height: 791px;
  }
  .headline {
    position: absolute;
    left: 60px;
    top: 62px;
    font-family: "Anton", "Oswald", sans-serif;
    font-size: 92px;
    line-height: 88px;
    letter-spacing: 0.5px;
    color: var(--ink);
    text-transform: uppercase;
    transform: scaleX(0.94);
    transform-origin: left top;
  }
  .business-name {
    position: absolute;
    left: 60px;
    top: 278px;
    font-family: "Barlow Semi Condensed", "Barlow Condensed", sans-serif;
    font-style: italic;
    font-weight: 800;
    font-size: 46px;
    line-height: 56px;
    color: var(--brand-green);
  }
  .services {
    position: absolute;
    left: 60px;
    top: 516px;
    font-family: "Barlow Condensed", sans-serif;
    font-weight: 500;
    font-size: 50px;
    line-height: 58px;
    color: var(--ink);
  }
  .call-to-action {
    position: absolute;
    left: 60px;
    top: 690px;
    display: flex;
    gap: 34px;
    font-family: "Barlow Condensed", sans-serif;
    font-style: italic;
    font-weight: 800;
    font-size: 52px;
    line-height: 56px;
  }
  .call-to-action .cta-label { color: var(--brand-green); }
  .call-to-action .cta-phone { color: var(--paper); }
</style>
</head>
<body>
<div class="ad">
  <svg class="ad-shapes" viewBox="0 0 1656 1028" preserveAspectRatio="none" aria-hidden="true">
    <rect class="top-field" x="0" y="0" width="1656" height="600" fill="var(--brand-green)"/>
    <path class="lower-field" d="M0 470 Q430 610 948 432 L1656 432 L1656 1028 L0 1028 Z" fill="var(--paper)"/>
    <path class="swoosh" d="M0 488 Q480 700 948 458 Q470 590 0 545 Z" fill="var(--ink)"/>
    <rect class="footer-band" x="0" y="863" width="1656" height="165" fill="var(--ink)"/>
    <path class="name-pill" d="M0 338 L802 338 A56 56 0 0 1 802 450 L0 450 Z" fill="var(--paper)"/>
    <ellipse class="photo-frame" cx="1318" cy="515" rx="455" ry="458" fill="var(--paper)"/>
  </svg>
  <svg class="ad-photo" viewBox="0 0 1656 1028" preserveAspectRatio="none" role="img" aria-label="Photo of two people checking a stack of cardboard boxes on a cart in a hallway of green storage units">
    <defs>
      <linearGradient id="photoTone" x1="0" y1="0" x2="1" y2="1">
        <stop offset="0" stop-color="var(--photo-light)"/>
        <stop offset="0.45" stop-color="var(--photo-mid)"/>
        <stop offset="1" stop-color="var(--photo-warm)"/>
      </linearGradient>
    </defs>
    <ellipse cx="1320" cy="512" rx="435" ry="436" fill="url(#photoTone)"/>
  </svg>

  <h1 class="headline">Your only storage<br>in Port Ludlow.</h1>
  <p class="business-name">Cedar Hollow Mini Storage</p>
  <p class="services">Units &amp; Outdoor Parking for Boats,<br>RVs &amp; Trailers. (Small Subhead)</p>
  <p class="call-to-action"><span class="cta-label">CALL US TODAY!</span><span class="cta-phone">360-555-0147</span></p>
</div>
</body>
</html>
```